Professional consulting firm needing a Word document template

I need a Word document template that can be used flexibly for a flyer or brochure of 1 to 3 pages in length. The first page should be designed in a way that it can stand alone as a one-page flyer without a formal cover page. I have attached sample text as a Word document that could be used as the basis for the first 1-2 pages, however I do need three page layouts designed to give flexibility to use as a 3 page booklet. I have attached our brand guidelines, logo, and some stock images that I have previously purchased (they may not all be useful but it gives some options). <br/>The Word document needs to be set up in away that it can easily be edited to accommodate updates to the text, and some variation in the quantity of text on each page. Each page should be able to accommodate a mixture of paragraph text, bullet points, small boxes to call out highlights, one or more images, and some white space to avoid clutter. It should look professional yet engaging and modern.

Font styles to use
Sans Serif

Requirements
Must have
• Must be an editable Microsoft Word document, using the text provided. Must be a layout suitable to use as 1 page, up to 3 pages. Must comply with brand guidelines.

```html
<!DOCTYPE html>
<html lang="en">
<head>
<meta charset="utf-8">
<title>Train Driver Competency Indicator Development Project – Brochure Template</title>
<link href="https://fonts.googleapis.com/css2?family=Carlito:wght@400;700&family=Lato:wght@400;700&display=swap" rel="stylesheet">
<style>
  :root {
    --backdrop: #f1f1ef;
    --paper: #ffffff;
    --ink: #2b2f33;
    --ink-soft: #3a3f44;
    --teal: #2bb3d6;
    --teal-light: #7fd2ea;
    --pill: #c4e8f8;
    --navy: #0f2231;
    --brand: #1d2b36;
    --rule: #cfe9f4;
  }
  * { box-sizing: border-box; margin: 0; padding: 0; }
  html, body { width: 885px; height: 1200px; overflow: hidden; }
  body {
    background: var(--backdrop);
    font-family: "Carlito", "Calibri", sans-serif;
    color: var(--ink);
    position: relative;
  }
  h1, h2, h3 { font-weight: 400; }

  .page { position: absolute; width: 393px; height: 556px; background: var(--paper); overflow: hidden; }
  .page--cover { left: 32px; top: 29px; }
  .page--two { left: 457px; top: 29px; }
  .page--three { left: 32px; top: 613px; }
  .page--four { left: 457px; top: 613px; }

  .corner-pattern {
    position: absolute; left: -14px; top: -16px; width: 72px; height: 82px; border-radius: 50%;
    background: radial-gradient(circle at 40% 40%, var(--teal-light), var(--teal) 70%, #8fd7ec);
    opacity: .85;
  }
  .corner-pattern--large { width: 92px; height: 104px; }

  /* Cover */
  .cover-title {
    position: absolute; right: 21px; top: 35px;
    text-align: right; font-family: "Lato", Arial, sans-serif; font-size: 14.5px; line-height: 22px;
    color: var(--navy); text-transform: uppercase;
  }
  .cover-band { position: absolute; left: 0; right: 0; top: 109px; height: 19px; background: var(--navy); border-bottom: 3px solid var(--teal); }
  .cover-photo {
    position: absolute; left: 0; right: 0; top: 131px; height: 396px;
    background: linear-gradient(160deg, #1a3a4c 0%, #2c8fb5 25%, #7ccf3a 45%, #1b7fbf 60%, #0d2d45 75%, #8fc3db 100%);
  }
  .cover-brand {
    position: absolute; left: 10px; top: 396px;
    font-family: "Lato", Arial, sans-serif; font-size: 23px; font-weight: 700; letter-spacing: 1.5px; color: var(--brand);
  }
  .cover-footer {
    position: absolute; left: 0; right: 0; bottom: 0; height: 29px;
    display: flex; align-items: center; justify-content: space-between;
    padding: 0 22px 0 27px; font-size: 7.2px; color: var(--ink);
    border-bottom: 3px solid var(--pill);
  }
  .contact { display: flex; align-items: center; gap: 5px; white-space: nowrap; }
  .contact svg { width: 10px; height: 10px; flex: none; }

  /* Inner pages */
  .page-header {
    position: absolute; left: 51px; right: 0; top: 33px;
    font-family: "Lato", Arial, sans-serif; font-size: 9px; color: var(--navy); text-transform: uppercase;
    border-bottom: 1px solid var(--rule); padding-bottom: 1px;
  }
  .page-header--section { left: 48px; text-transform: none; }
  .copy { position: absolute; left: 47px; width: 294px; font-size: 7px; line-height: 14.6px; color: var(--ink-soft); }
  .copy--dense { line-height: 12px; }
  .copy--p3 { left: 48px; width: 300px; line-height: 12px; }
  .intro { top: 45px; }

  .competencies { position: absolute; top: 115px; list-style: none; font-size: 7px; line-height: 15px; color: var(--ink-soft); }
  .competencies--left { left: 64px; width: 150px; }
  .competencies--right { left: 224px; width: 130px; }
  .competencies li { position: relative; padding-left: 12px; }
  .competencies li::before { content: ""; position: absolute; left: 0; top: 6px; width: 3px; height: 3px; border-radius: 50%; background: var(--teal); }

  .callout {
    position: absolute; left: 47px; top: 220px; width: 290px; height: 66px;
    border: 1px solid var(--teal); border-radius: 4px; padding: 5px 7px;
    font-size: 6.6px; line-height: 12px; color: var(--ink-soft);
  }
  .callout-title { color: var(--teal); font-size: 7px; }
  .subheading { position: absolute; left: 47px; top: 390px; font-family: "Lato", Arial, sans-serif; font-size: 7.8px; color: var(--navy); }

  .involved { position: absolute; left: 56px; top: 86px; width: 300px; list-style: none; font-size: 6.8px; line-height: 11.2px; color: var(--ink-soft); }
  .involved li { position: relative; padding-left: 12px; }
  .involved li::before { content: ""; position: absolute; left: 0; top: 4px; width: 3px; height: 3px; background: var(--teal); }
  .involved .lead { color: var(--teal); }

  .feature-photo {
    position: absolute; left: 51px; top: 240px; width: 291px; height: 139px;
    background: linear-gradient(170deg, #c44a2c 0%, #2d7ea8 20%, #82d23a 40%, #16335a 55%, #a9dcea 70%, #e4f4f8 100%);
  }

  .page-footer { position: absolute; left: 17px; right: 14px; top: 512px; height: 18px; display: flex; align-items: center; }
  .page-number {
    width: 18px; height: 18px; border-radius: 50%; background: var(--pill); flex: none;
    font-size: 5.5px; font-weight: 700; display: flex; align-items: center; justify-content: center; color: var(--navy);
  }
  .footer-pill {
    margin-left: 14px; width: 243px; height: 15px; border-radius: 8px; background: var(--pill);
    display: flex; align-items: center; gap: 14px; padding-left: 8px; font-size: 6px; color: var(--navy);
  }
  .footer-pill .contact svg { width: 8px; height: 8px; }
  .footer-brand { margin-left: auto; font-family: "Lato", Arial, sans-serif; font-size: 11px; font-weight: 700; letter-spacing: .8px; color: var(--brand); }
</style>
</head>
<body>

<!-- Page 1: cover / stand-alone flyer -->
<section class="page page--cover">
  <div class="corner-pattern corner-pattern--large" role="img" aria-label="Decorative cluster of blue circles"></div>
  <h1 class="cover-title">Train Driver Competency Indicator<br>Development Project</h1>
  <div class="cover-band"></div>
  <div class="cover-photo" role="img" aria-label="Long-exposure photo of a train speeding through a station"></div>
  <div class="cover-brand">TRACKSENSE</div>
  <footer class="cover-footer">
    <span class="contact"><svg viewBox="0 0 24 24"><path fill="#1d2b36" d="M6.6 10.8a15.1 15.1 0 0 0 6.6 6.6l2.2-2.2a1 1 0 0 1 1-.25 11.4 11.4 0 0 0 3.6.6 1 1 0 0 1 1 1V20a1 1 0 0 1-1 1A17 17 0 0 1 3 4a1 1 0 0 1 1-1h3.5a1 1 0 0 1 1 1c0 1.25.2 2.45.6 3.6a1 1 0 0 1-.25 1z"/></svg>0400 218 365</span>
    <span class="contact"><svg viewBox="0 0 24 24"><circle cx="12" cy="12" r="10" fill="none" stroke="#1d2b36" stroke-width="2"/><path d="M2 12h20M12 2c3 3 3 17 0 20M12 2c-3 3-3 17 0 20" fill="none" stroke="#1d2b36" stroke-width="1.6"/></svg>www.tracksense-rail.com.au</span>
    <span class="contact"><svg viewBox="0 0 24 24"><rect x="2" y="5" width="20" height="14" fill="none" stroke="#1d2b36" stroke-width="2"/><path d="M2 5l10 8 10-8" fill="none" stroke="#1d2b36" stroke-width="2"/></svg>hello@tracksense-rail.com.au</span>
  </footer>
</section>

<!-- Page 2 -->
<section class="page page--two">
  <div class="corner-pattern" role="img" aria-label="Decorative cluster of blue circles"></div>
  <h2 class="page-header">Train Driver Competency Indicator Development Project</h2>
  <p class="copy intro">We are commencing an applied research project to develop and test a framework of underlying core competencies for train driver performance. The objective of the project is to identify observable indicators that describe effective performance in the following types of underlying competencies:</p>
  <ul class="competencies competencies--left">
    <li>Application of Procedures</li>
    <li>Communication</li>
    <li>Operation of Tools / Equipment</li>
    <li>Problem Solving and Decision<br>Making</li>
    <li>Route Knowledge</li>
  </ul>
  <ul class="competencies competencies--right">
    <li>Self-Management</li>
    <li>Situation Awareness</li>
    <li>System Knowledge</li>
    <li>Teamwork and Leadership</li>
    <li>Train Handling</li>
    <li>Workload Management</li>
  </ul>
  <div class="callout">
    <div class="callout-title">Underlying competencies:</div>
    The underpinning knowledge and skills required by a train driver, to perform a range of different tasks effectively. Underlying competencies include both ‘technical’ and ‘non-technical’ skills. They are not specific to one driving task, but help build resilient performance across all tasks, conditions or situations that a driver may encounter.
  </div>
  <p class="copy" style="top:303px">In contrast to other performance marker systems, the current project aims to include both ‘technical’ and ‘non-technical’ skills in an integrated framework, with substantial input from drivers across the industry, both in passenger and freight operations. The aim is to develop a framework that uses a language that describes performance in a way that is relatable to drivers, trainers, and assessors.</p>
  <h3 class="subheading">What are the benefits for participating organisations?</h3>
  <p class="copy copy--dense" style="top:409px">All participating rail organisations will receive a copy of the performance indicator framework, which they are free to use or adapt for application within their own operation. A summary report will also be provided, outlining the methodology and aggregated results of the data collection activities. All results will be presented in a de-identified way, to ensure the anonymity of participating organisations and individuals.</p>
  <footer class="page-footer">
    <span class="page-number">2</span>
    <span class="footer-pill">
      <span class="contact"><svg viewBox="0 0 24 24"><circle cx="12" cy="12" r="10" fill="none" stroke="#1d2b36" stroke-width="2"/><path d="M2 12h20M12 2c3 3 3 17 0 20M12 2c-3 3-3 17 0 20" fill="none" stroke="#1d2b36" stroke-width="1.6"/></svg>www.tracksense-rail.com.au</span>
      <span class="contact"><svg viewBox="0 0 24 24"><rect x="2" y="5" width="20" height="14" fill="#1d2b36"/><path d="M2 5l10 8 10-8" fill="none" stroke="#fff" stroke-width="2"/></svg>hello@tracksense-rail.com.au</span>
    </span>
    <span class="footer-brand">TRACKSENSE</span>
  </footer>
</section>

<!-- Page 3 -->
<section class="page page--three">
  <div class="corner-pattern" role="img" aria-label="Decorative cluster of blue circles"></div>
  <h2 class="page-header page-header--section">What is involved?</h2>
  <p class="copy copy--p3" style="top:50px">Participating organisations will be invited to provide in-kind support for the following activities during the period April – June 2020:</p>
  <ul class="involved">
    <li><span class="lead">Interviews with volunteer Driver participants:</span> individual discussions with our researchers about drivers’ previous experiences, to gather information about expert driving strategies and positive techniques used in normal and abnormal operations.</li>
    <li><span class="lead">Initial workshop</span>: a facilitated group workshop to understand the links between underlying competencies and driving tasks, and to understand Drivers’ perceptions of what each underlying competency looks like in practice.</li>
    <li><span class="lead">Driver Training Survey</span>: a voluntary survey will be distributed, requesting Driver Trainers’ and Assessors’ views on the importance of underlying competencies in driving performance, and further data about expert strategies and techniques.</li>
    <li><span class="lead">Follow-up workshop:</span> a facilitated group workshop to test and refine the performance indicators. Where possible, indicators will be tested through participants providing ratings of a video sample of actual performance, to determine whether multiple raters can distinguish between competency categories.</li>
  </ul>
  <p class="copy copy--p3" style="top:242px">It is anticipated that workshops will be run in Brisbane, Sydney and Melbourne. We would appreciate support from participating organisations in providing a workshop venue where possible. Apart from the in-kind support of providing access to personnel and a meeting room, there is no cost associated with participation in the project.</p>
  <p class="copy copy--p3" style="top:302px">In addition to the activities involving industry participation, we will also be completing a detailed task analysis and analysing incident reports and other publicly available data, to help inform the development of the framework.</p>
  <p class="copy copy--p3" style="top:350px">We look forward to hearing from organisations interested in being part of this landmark project.</p>
  <footer class="page-footer">
    <span class="page-number">3</span>
    <span class="footer-pill">
      <span class="contact"><svg viewBox="0 0 24 24"><circle cx="12" cy="12" r="10" fill="none" stroke="#1d2b36" stroke-width="2"/><path d="M2 12h20M12 2c3 3 3 17 0 20M12 2c-3 3-3 17 0 20" fill="none" stroke="#1d2b36" stroke-width="1.6"/></svg>www.tracksense-rail.com.au</span>
      <span class="contact"><svg viewBox="0 0 24 24"><rect x="2" y="5" width="20" height="14" fill="#1d2b36"/><path d="M2 5l10 8 10-8" fill="none" stroke="#fff" stroke-width="2"/></svg>hello@tracksense-rail.com.au</span>
    </span>
    <span class="footer-brand">TRACKSENSE</span>
  </footer>
</section>

<!-- Page 4 -->
<section class="page page--four">
  <div class="corner-pattern" role="img" aria-label="Decorative cluster of blue circles"></div>
  <h2 class="page-header">Train Driver Competency Indicator Development Project</h2>
  <p class="copy intro">We are commencing an applied research project to develop and test a framework of underlying core competencies for train driver performance. The objective of the project is to identify observable indicators that describe effective performance in the following types of underlying competencies:</p>
  <ul class="competencies competencies--left">
    <li>Application of Procedures</li>
    <li>Communication</li>
    <li>Operation of Tools / Equipment</li>
    <li>Problem Solving and Decision<br>Making</li>
    <li>Route Knowledge</li>
  </ul>
  <ul class="competencies competencies--right">
    <li>Self-Management</li>
    <li>Situation Awareness</li>
    <li>System Knowledge</li>
    <li>Teamwork and Leadership</li>
    <li>Train Handling</li>
    <li>Workload Management</li>
  </ul>
  <div class="feature-photo" role="img" aria-label="Photo of a train blurring past an empty station platform"></div>
  <footer class="page-footer">
    <span class="page-number">4</span>
    <span class="footer-pill">
      <span class="contact"><svg viewBox="0 0 24 24"><circle cx="12" cy="12" r="10" fill="none" stroke="#1d2b36" stroke-width="2"/><path d="M2 12h20M12 2c3 3 3 17 0 20M12 2c-3 3-3 17 0 20" fill="none" stroke="#1d2b36" stroke-width="1.6"/></svg>www.tracksense-rail.com.au</span>
      <span class="contact"><svg viewBox="0 0 24 24"><rect x="2" y="5" width="20" height="14" fill="#1d2b36"/><path d="M2 5l10 8 10-8" fill="none" stroke="#fff" stroke-width="2"/></svg>hello@tracksense-rail.com.au</span>
    </span>
    <span class="footer-brand">TRACKSENSE</span>
  </footer>
</section>

</body>
</html>
```